Homepage of voice message app

We are developing a mobile application of which one of the more important features is a voice to transcript.

What we would like to have designed is a basic interface that would show one ore more avatars on a home screen + the following functionalities:
- record
-while recording there should be three functions included in buttons (delete last sentence / send / send & next message (i.e. keep the recording going))
&
- listen (to new message)
- while listening replies should be possible in the form of emoticons (only emoticons, no text)

Attached:
-an example of the style we appreciate

Target Market(s)

English speaking Millenials

Industry/Entity Type

Messaging

Font styles to use
Sans Serif

Requirements
Must have
• My project must have a clean design and should not be too futuristic. We are targetting an average person between 20-80 years.
Nice to have
• We would like to focus on a minimum amount of finger movements to get the message across, we prefer simple tabs and swipes within the home screen to access the features.
Should not have
• The project should not have too many moving pieces within the screen.

```html
<!DOCTYPE html>
<html lang="en">
<head>
<meta charset="utf-8">
<title>Voice Message App – Screen Flow</title>
<link href="https://fonts.googleapis.com/css2?family=Montserrat:wght@400;500;600&display=swap" rel="stylesheet">
<style>
  :root {
    --board-bg: #e6e9f0;
    --panel-blue: #2f5aae;
    --status-blue: #6f86bd;
    --tab-slate: #455468;
    --nav-dark: #2b2b2b;
    --mic-red: #d94b5a;
    --pulse-pink: #f7939b;
    --stop-red: #d94b5a;
    --trash-dark: #2a1d10;
    --send-green: #2a8a16;
    --send-next-purple: #7b12a6;
    --pill-plum: #8a1f6e;
    --reaction-ring: #284c8f;
    --reaction-fill: #f5c33b;
    --ink: #3c3c3c;
    --label-ink: #5a5a5a;
    --white: #ffffff;
  }
  html, body {
    margin: 0;
    padding: 0;
    width: 1200px;
    height: 720px;
    overflow: hidden;
    background: var(--board-bg);
    font-family: "Montserrat", sans-serif;
  }
  .board {
    position: relative;
    width: 1200px;
    height: 720px;
  }
  .screen {
    position: absolute;
    top: 128px;
    width: 163px;
    height: 327px;
    box-shadow: 0 6px 18px rgba(40, 50, 80, 0.18);
  }
  .screen svg { display: block; width: 163px; height: 327px; }
  .screen text { font-family: "Montserrat", sans-serif; }
  .step {
    position: absolute;
    top: 523px;
    width: 260px;
    margin-left: -130px;
    text-align: center;
  }
  .step-number {
    width: 48px;
    height: 48px;
    margin: 0 auto;
    border: 1px solid #b9bcc4;
    border-radius: 50%;
    background: var(--white);
    color: var(--label-ink);
    font-size: 20px;
    line-height: 48px;
    font-weight: 500;
  }
  .step-title {
    margin-top: 20px;
    color: var(--label-ink);
    font-size: 25px;
    font-weight: 500;
    letter-spacing: 0.5px;
  }
</style>
</head>
<body>
<svg width="0" height="0" style="position:absolute">
  <defs>
    <g id="status-bar">
      <rect x="0" y="0" width="336" height="16" fill="#6f86bd"/>
      <path d="M232 4 l10 0 l-5 7 z" fill="#fff"/>
      <path d="M246 11 l10 -8 l0 8 z" fill="#fff"/>
      <rect x="262" y="4" width="6" height="8" fill="#fff"/>
      <text x="310" y="12" font-size="10" fill="#fff" text-anchor="middle">12:30</text>
    </g>
    <g id="header">
      <rect x="0" y="16" width="336" height="657" fill="#fff"/>
      <text x="168" y="96" font-size="21" fill="#3c3c3c" text-anchor="middle" font-weight="500" letter-spacing="0.5">Welcome</text>
      <text x="166" y="148" font-size="11" fill="#222" text-anchor="middle">Mara Ellison</text>
      <circle cx="166" cy="196" r="42" fill="#7a7a7a" stroke="#2f6fd6" stroke-width="2.5"/>
    </g>
    <g id="nav-bar">
      <rect x="0" y="643" width="336" height="30" fill="#2b2b2b"/>
      <path d="M79 653 l0 10 l-8 -5 z" fill="none" stroke="#ddd" stroke-width="1.2"/>
      <circle cx="168" cy="658" r="5" fill="none" stroke="#ddd" stroke-width="1.2"/>
      <rect x="258" y="654" width="9" height="9" fill="none" stroke="#ddd" stroke-width="1.2"/>
    </g>
    <g id="pause-ring">
      <circle cx="0" cy="0" r="17" fill="none" stroke="#fff" stroke-width="3"/>
      <rect x="-6" y="-7" width="4" height="14" rx="1" fill="#fff"/>
      <rect x="2" y="-7" width="4" height="14" rx="1" fill="#fff"/>
    </g>
    <g id="play-mark"><path d="M0 -8 l14 8 l-14 8 z" fill="#fff"/></g>
    <g id="send-mark"><path d="M-10 0 l20 -10 l-8 20 l-3 -8 z" fill="#fff"/></g>
  </defs>
</svg>

<main class="board">

  <!-- Homescreen -->
  <section class="screen" style="left:110px">
    <svg viewBox="0 0 336 673">
      <use href="#header"/>
      <use href="#status-bar"/>
      <path d="M0 370 q0 -12 12 -12 h312 q12 0 12 12 v273 h-336 z" fill="var(--panel-blue)"/>
      <g role="img" aria-label="Profile photo of the contact"><circle cx="166" cy="196" r="42" fill="#707070" stroke="#2f6fd6" stroke-width="2.5"/></g>
      <circle cx="165" cy="465" r="35" fill="var(--mic-red)"/>
      <rect x="159" y="446" width="12" height="22" rx="6" fill="#fff"/>
      <path d="M153 462 a12 12 0 0 0 24 0" fill="none" stroke="#fff" stroke-width="2.5"/>
      <rect x="163.5" y="474" width="3" height="8" fill="#fff"/>
      <g transform="translate(261 465)" fill="none" stroke="#fff" stroke-width="2">
        <circle r="5"/>
        <path d="M-2 -14 h4 l1 4 l4 -2 l3 3 l-2 4 l4 1 v4 l-4 1 l2 4 l-3 3 l-4 -2 l-1 4 h-4 l-1 -4 l-4 2 l-3 -3 l2 -4 l-4 -1 v-4 l4 -1 l-2 -4 l3 -3 l4 2 z"/>
      </g>
      <text x="168" y="531" font-size="15" fill="#fff" text-anchor="middle">Tap to begin</text>
      <rect x="168" y="587" width="168" height="56" fill="var(--tab-slate)"/>
      <text x="84" y="620" font-size="14" fill="#fff" text-anchor="middle">Record</text>
      <text x="252" y="620" font-size="14" fill="#fff" text-anchor="middle">Listen</text>
      <use href="#nav-bar"/>
    </svg>
  </section>

  <!-- Recording -->
  <section class="screen" style="left:379px">
    <svg viewBox="0 0 336 673">
      <use href="#header"/>
      <use href="#status-bar"/>
      <path d="M0 304 q0 -12 12 -12 h312 q12 0 12 12 v339 h-336 z" fill="var(--panel-blue)"/>
      <g role="img" aria-label="Profile photo of the contact"><circle cx="166" cy="196" r="42" fill="#707070" stroke="#2f6fd6" stroke-width="2.5"/></g>
      <use href="#pause-ring" transform="translate(61 392)"/>
      <circle cx="164" cy="392" r="52" fill="var(--pulse-pink)"/>
      <circle cx="164" cy="392" r="35" fill="var(--mic-red)"/>
      <g stroke="#fff" stroke-width="1.5" stroke-linecap="round">
        <line x1="148" y1="389" x2="148" y2="395"/><line x1="152" y1="386" x2="152" y2="398"/>
        <line x1="156" y1="388" x2="156" y2="396"/><line x1="160" y1="383" x2="160" y2="401"/>
        <line x1="164" y1="380" x2="164" y2="404"/><line x1="168" y1="384" x2="168" y2="400"/>
        <line x1="172" y1="387" x2="172" y2="397"/><line x1="176" y1="385" x2="176" y2="399"/>
        <line x1="180" y1="389" x2="180" y2="395"/>
      </g>
      <circle cx="267" cy="392" r="19" fill="none" stroke="#fff" stroke-width="3"/>
      <rect x="260" y="385" width="14" height="14" rx="2" fill="var(--stop-red)"/>
      <text x="168" y="478" font-size="14" fill="#fff" text-anchor="middle">Recording...</text>
      <circle cx="73" cy="580" r="28" fill="var(--trash-dark)"/>
      <g fill="none" stroke="#fff" stroke-width="1.8">
        <rect x="67" y="574" width="12" height="14" rx="1"/>
        <line x1="64" y1="573" x2="82" y2="573"/><line x1="70" y1="570" x2="76" y2="570"/>
        <line x1="71" y1="577" x2="71" y2="585"/><line x1="75" y1="577" x2="75" y2="585"/>
      </g>
      <circle cx="168" cy="580" r="28" fill="var(--send-green)"/>
      <use href="#send-mark" transform="translate(168 580)"/>
      <circle cx="263" cy="580" r="28" fill="var(--send-next-purple)"/>
      <use href="#send-mark" transform="translate(261 580)"/>
      <path d="M268 585 h8 M272 581 v8" stroke="#fff" stroke-width="1.6"/>
      <use href="#nav-bar"/>
    </svg>
  </section>

  <!-- Listening -->
  <section class="screen" style="left:649px">
    <svg viewBox="0 0 336 673">
      <use href="#header"/>
      <use href="#status-bar"/>
      <path d="M0 304 q0 -12 12 -12 h312 q12 0 12 12 v339 h-336 z" fill="var(--panel-blue)"/>
      <g role="img" aria-label="Profile photo of the contact"><circle cx="166" cy="196" r="42" fill="#707070" stroke="#2f6fd6" stroke-width="2.5"/></g>
      <text x="168" y="340" font-size="14" fill="#fff" text-anchor="middle">Your Recent Recordings</text>
      <text x="168" y="365" font-size="8" fill="#fff" text-anchor="middle">Tap &amp; Hold a recording for more options</text>
      <rect x="35" y="398" width="266" height="45" rx="22.5" fill="var(--pill-plum)"/>
      <use href="#play-mark" transform="translate(65 420)"/>
      <text x="96" y="425" font-size="14" fill="#fff">Recording 1</text>
      <rect x="35" y="458" width="266" height="45" rx="22.5" fill="var(--pill-plum)"/>
      <use href="#play-mark" transform="translate(65 480)"/>
      <text x="96" y="485" font-size="14" fill="#fff">Recording 2</text>
      <rect x="35" y="518" width="266" height="45" rx="22.5" fill="var(--pill-plum)"/>
      <use href="#play-mark" transform="translate(65 540)"/>
      <text x="96" y="545" font-size="14" fill="#fff">Recording 3</text>
      <rect x="0" y="587" width="168" height="56" fill="var(--tab-slate)"/>
      <text x="84" y="620" font-size="14" fill="#fff" text-anchor="middle">Record</text>
      <text x="252" y="620" font-size="14" fill="#fff" text-anchor="middle">Listen</text>
      <use href="#nav-bar"/>
    </svg>
  </section>

  <!-- Listening Details -->
  <section class="screen" style="left:918px">
    <svg viewBox="0 0 336 673">
      <use href="#header"/>
      <use href="#status-bar"/>
      <path d="M0 304 q0 -12 12 -12 h312 q12 0 12 12 v339 h-336 z" fill="var(--panel-blue)"/>
      <g role="img" aria-label="Profile photo of the contact"><circle cx="166" cy="196" r="42" fill="#707070" stroke="#2f6fd6" stroke-width="2.5"/></g>
      <text x="33" y="338" font-size="14" fill="#fff">Now Playing</text>
      <text x="33" y="384" font-size="21" fill="#fff" font-weight="500">Recording 1</text>
      <use href="#pause-ring" transform="translate(57 455)"/>
      <g stroke="#fff" stroke-width="3" stroke-linecap="round">
        <line x1="113" y1="447" x2="113" y2="463"/><line x1="121" y1="440" x2="121" y2="470"/>
        <line x1="129" y1="432" x2="129" y2="478"/><line x1="137" y1="448" x2="137" y2="462"/>
        <line x1="145" y1="443" x2="145" y2="467"/><line x1="153" y1="436" x2="153" y2="474"/>
        <line x1="161" y1="428" x2="161" y2="482"/><line x1="169" y1="420" x2="169" y2="490"/>
        <line x1="177" y1="430" x2="177" y2="480"/><line x1="185" y1="444" x2="185" y2="466"/>
        <line x1="193" y1="434" x2="193" y2="476"/><line x1="201" y1="442" x2="201" y2="468"/>
        <line x1="209" y1="448" x2="209" y2="462"/><line x1="217" y1="450" x2="217" y2="460"/>
      </g>
      <circle cx="69" cy="586" r="34" fill="var(--reaction-ring)"/>
      <circle cx="69" cy="586" r="22" fill="var(--reaction-fill)" role="img" aria-label="Smiling reaction emoji"/>
      <circle cx="168" cy="586" r="34" fill="var(--reaction-ring)"/>
      <circle cx="168" cy="586" r="22" fill="var(--reaction-fill)" role="img" aria-label="Nerdy glasses reaction emoji"/>
      <circle cx="266" cy="586" r="34" fill="var(--reaction-ring)"/>
      <circle cx="266" cy="586" r="22" fill="var(--reaction-fill)" role="img" aria-label="Star-struck reaction emoji"/>
      <use href="#nav-bar"/>
    </svg>
  </section>

  <div class="step" style="left:192px"><div class="step-number">1</div><div class="step-title">Homescreen</div></div>
  <div class="step" style="left:461px"><div class="step-number">2</div><div class="step-title">Recording</div></div>
  <div class="step" style="left:730px"><div class="step-number">3</div><div class="step-title">Listening</div></div>
  <div class="step" style="left:999px"><div class="step-number">3.1</div><div class="step-title">Listening Details</div></div>

</main>
</body>
</html>
```